shutter business card and postcard design

Custom Interior and Exterior Shutters manufactured In Houston Texas Made in USA we offer fast delivery lifetime warranty
Dale Whitcombe owner has been manufacturing shutters in houston for over 44 years
nedd to use one of the pictures provided and add company name phone number on face Louver Crest (281)555-7384
back side
louver crest
2317 quillfeather ln.
houston, texas 77999
email louvercrest@mailnest.example
website louvercresthouston.example

```html
<!DOCTYPE html>
<html lang="en">
<head>
<meta charset="utf-8">
<title>Louver Crest – Custom Interior &amp; Exterior Shutters</title>
<link rel="stylesheet" href="https://fonts.googleapis.com/css2?family=Mulish:wght@800&family=Questrial&family=Signika:wght@400;600;700&display=swap">
<style>
  :root {
    --teal-deep: #0e4d53;
    --teal-mid: #165d63;
    --teal-soft: #5f8f93;
    --teal-mist: #c9dfe1;
    --white: #ffffff;
    --band-grey: #d9dcdd;
    --card-text: #1f6a70;
  }
  * { box-sizing: border-box; margin: 0; padding: 0; }
  html, body { width: 1200px; height: 801px; overflow: hidden; background: var(--teal-deep); }
  .postcard { position: relative; width: 1200px; height: 801px; overflow: hidden; font-family: "Questrial", sans-serif; }
  .backdrop { position: absolute; inset: 0; width: 1200px; height: 801px; }

  .hero-photo {
    position: absolute; left: 632px; top: -4px; width: 530px; height: 227px;
    border: 2px solid var(--white); border-radius: 14px;
    background: linear-gradient(135deg, #55605c 0%, #8f9690 35%, #c9cfcb 55%, #6b6a5c 80%, #3f423d 100%);
  }

  .brand-name {
    position: absolute; left: 122px; top: 132px;
    font-family: "Signika", sans-serif; font-weight: 700; font-size: 62px; line-height: 64px;
    color: var(--teal-deep); letter-spacing: 2px; text-transform: uppercase;
  }

  .tagline-band {
    position: absolute; left: 122px; top: 286px; width: 752px; height: 62px;
    background: linear-gradient(90deg, var(--teal-mid) 0%, rgba(22,93,99,0.75) 60%, rgba(22,93,99,0) 100%);
    color: var(--white); font-size: 37px; line-height: 62px; padding-left: 19px;
  }

  .benefits { position: absolute; left: 139px; top: 372px; list-style: none; }
  .benefits li {
    font-family: "Mulish", sans-serif; font-weight: 800; font-size: 29px; color: var(--white);
    height: 53px; line-height: 36px; display: flex; align-items: center; gap: 12px;
  }
  .benefits li::before { content: ""; width: 15px; height: 15px; background: var(--white); flex: none; }

  .contact-card {
    position: absolute; left: 632px; top: 476px; width: 528px; height: 340px;
    background: var(--white); border-radius: 18px; color: var(--card-text);
  }
  .contact-card .company {
    position: absolute; left: 30px; top: 20px;
    font-family: "Signika", sans-serif; font-weight: 600; font-size: 27px; color: var(--teal-deep); letter-spacing: 0.5px;
  }
  .contact-card .owner { position: absolute; left: 30px; top: 58px; font-size: 24px; letter-spacing: 0.3px; }
  .contact-card .owner small { font-size: 20px; }
  .contact-line { position: absolute; left: 30px; display: flex; gap: 6px; font-size: 26px; line-height: 33px; }
  .contact-line svg { flex: none; margin-top: 6px; }
  .address { top: 104px; }
  .phone { top: 180px; }
  .email { top: 225px; font-size: 27px; }
  .website {
    position: absolute; left: 32px; top: 264px; width: 463px; height: 80px;
    background: var(--teal-deep); border-radius: 18px; color: var(--white);
    font-family: "Mulish", sans-serif; font-weight: 800; font-size: 24px; text-align: center; line-height: 56px;
  }
</style>
</head>
<body>
<main class="postcard">
  <svg class="backdrop" viewBox="0 0 1500 1001" preserveAspectRatio="none" aria-hidden="true">
    <defs>
      <radialGradient id="houseGlow" cx="0.33" cy="0.2" r="0.75">
        <stop offset="0" stop-color="#cfe3e5"/>
        <stop offset="0.45" stop-color="#7fa8ab"/>
        <stop offset="1" stop-color="#3f7b80"/>
      </radialGradient>
      <linearGradient id="roofBand" x1="0" y1="0" x2="1" y2="1">
        <stop offset="0" stop-color="#ffffff"/>
        <stop offset="0.6" stop-color="#e6e8e8"/>
        <stop offset="1" stop-color="#cfd3d4"/>
      </linearGradient>
    </defs>
    <rect width="1500" height="1001" fill="var(--teal-deep)"/>
    <polygon points="0,240 290,40 1500,650 1500,1001 0,1001" fill="url(#houseGlow)"/>
    <polygon points="0,160 232,0 360,0 1500,575 1500,650 290,40 0,240" fill="url(#roofBand)"/>
  </svg>

  <div class="hero-photo" role="img" aria-label="Photo of a study with tall arched windows fitted with white plantation shutters"></div>

  <div class="brand-name">Louver<br>Crest</div>

  <div class="tagline-band">Custom Interior &amp; Exterior Shutters</div>

  <ul class="benefits">
    <li>Manufacturing shutters in houston for over 44 years</li>
    <li>Fast Delivery</li>
    <li>Lifetime Warranty</li>
  </ul>

  <section class="contact-card">
    <h2 class="company">LOUVER CREST</h2>
    <p class="owner">DALE WHITCOMBE <small>(OWNER)</small></p>
    <p class="contact-line address">
      <svg width="18" height="22" viewBox="0 0 18 22" aria-hidden="true"><path d="M9 1a7 7 0 0 0-7 7c0 5 7 13 7 13s7-8 7-13a7 7 0 0 0-7-7z" fill="none" stroke="var(--card-text)" stroke-width="2.5"/><circle cx="9" cy="8" r="2.5" fill="var(--card-text)"/></svg>
      <span>2317 Quillfeather ln.<br>Houston, Texas 77999</span>
    </p>
    <p class="contact-line phone">
      <svg width="20" height="28" viewBox="0 0 20 28" aria-hidden="true"><rect x="2" y="1.5" width="16" height="25" rx="3" fill="none" stroke="var(--card-text)" stroke-width="2.5"/><rect x="7" y="21" width="6" height="2" fill="var(--card-text)"/></svg>
      <span>(281)555-7384</span>
    </p>
    <p class="contact-line email">
      <svg width="24" height="18" viewBox="0 0 24 18" aria-hidden="true"><rect x="0" y="1" width="24" height="16" rx="2" fill="var(--card-text)"/><path d="M2 3l10 8 10-8M2 15l7-6M22 15l-7-6" stroke="var(--white)" stroke-width="1.8" fill="none"/></svg>
      <span>louvercrest@mailnest.example</span>
    </p>
    <div class="website">louvercresthouston.example</div>
  </section>
</main>
</body>
</html>
```